Plastic Surgeon Needs a business card desing

I need a plastic surgeon business card, Im young , innovative , not afraid of thinking out of the box, What I dont like is human figures or scalpes as designing the card, because I think they are old fashion, I think my name is my strongest card, so I try to find the desing to be something elegant , simple , slick , stylish , radiant with carimsa!

Target Market(s)

PLastics Surgery Patients and doctors to have my data

Industry/Entity Type

Plastic

Contact Information for Business Card

phone numbers need to be legible , right now i have grey scales so they a not to legible

Font styles to use
Serif
Sans Serif

Requirements
Must have
• Personality, and it has to look like a doctor card, not a buisness man card, that is why i think it should be clean , clear , and legible
Nice to have
• Stylilsh, not to heavy card, in means of colors and logos, i think it should give a sensation of health
• Im not sure to have the logo of the hospital i work
Should not have
• human figures
• Hands
• Surgeons

```html
<!DOCTYPE html>
<html lang="es">
<head>
<meta charset="utf-8">
<title>Dr. Mateo Rosales – Tarjeta de presentación</title>
<link href="https://fonts.googleapis.com/css2?family=Arimo:wght@400;500&display=swap" rel="stylesheet">
<style>
  :root {
    --bg: #e9e6e1;
    --card-white: #f7f7f7;
    --blue-light: #4a8fd8;
    --blue: #2e6cc3;
    --blue-deep: #1f52a3;
    --rule: #2e6cc3;
    --ink-blue: #4a72bf;
    --white: #ffffff;
  }
  * { margin: 0; padding: 0; box-sizing: border-box; }
  html, body { width: 1200px; height: 902px; overflow: hidden; }
  body {
    background: var(--bg);
    font-family: "Arimo", Arial, sans-serif;
    position: relative;
  }
  .card {
    position: absolute;
    width: 540px;
    height: 309px;
    background: var(--card-white);
    box-shadow: 0 6px 18px rgba(0,0,0,0.18);
    overflow: hidden;
  }
  .card--front { left: 40px; top: 120px; }
  .card--back  { left: 620px; top: 470px; }

  .band {
    position: absolute;
    left: 0; right: 0;
    background: linear-gradient(115deg, var(--blue-light) 0%, var(--blue) 45%, var(--blue-deep) 100%);
  }
  .rule {
    position: absolute;
    left: 0; right: 0;
    height: 2px;
    background: var(--rule);
  }

  /* front */
  .card--front .band { top: 124px; bottom: 0; }
  .card--front .rule { top: 118px; }
  .front-email {
    position: absolute;
    right: 36px; top: 96px;
    font-size: 13px;
    color: var(--ink-blue);
  }
  .identity {
    position: absolute;
    display: flex;
    align-items: center;
    gap: 18px;
  }
  .card--front .identity { left: 48px; top: 66px; }
  .mark { flex: none; }
  .name {
    font-size: 30px;
    font-weight: 500;
    color: var(--white);
    letter-spacing: 0.5px;
    line-height: 1;
  }
  .specialty {
    font-size: 15px;
    color: var(--white);
    margin-top: 6px;
  }

  /* back */
  .card--back .band { top: 0; height: 150px; }
  .card--back .rule { top: 154px; }
  .card--back .identity { left: 48px; top: 62px; }
  .contact {
    position: absolute;
    left: 230px; top: 178px;
    font-size: 12.5px;
    line-height: 1.45;
    color: var(--ink-blue);
    list-style: none;
    text-align: center;
  }
</style>
</head>
<body>
  <section class="card card--front" aria-label="Frente de la tarjeta">
    <p class="front-email">mateo@drrosales.com</p>
    <div class="rule"></div>
    <div class="band">
      <div class="identity">
        <svg class="mark" width="52" height="52" viewBox="0 0 52 52" aria-hidden="true">
          <circle cx="26" cy="26" r="24" fill="#e6eef8"/>
        </svg>
        <div>
          <h1 class="name">DR. MATEO ROSALES</h1>
          <p class="specialty">Cirugia plastica, estetica y reconstructiva</p>
        </div>
      </div>
    </div>
  </section>

  <section class="card card--back" aria-label="Reverso de la tarjeta">
    <div class="band">
      <div class="identity">
        <svg class="mark" width="52" height="52" viewBox="0 0 52 52" aria-hidden="true">
          <circle cx="26" cy="26" r="24" fill="#e6eef8"/>
        </svg>
        <div>
          <h2 class="name">DR. MATEO ROSALES</h2>
          <p class="specialty">Cirugia plastica, estetica y reconstructiva</p>
        </div>
      </div>
    </div>
    <div class="rule"></div>
    <ul class="contact">
      <li>Calle Olmos 2150, Int. 84</li>
      <li>Torre Medica Horizonte</li>
      <li>Guadalajara, Jalisco, Mexico</li>
      <li>P : 01 (33) 3555 0142</li>
      <li>C : 33 3555 0187</li>
      <li>E : mateo@drrosales.com</li>
    </ul>
  </section>
</body>
</html>
```